Bright Arch Group business card

Bright Arch Group is the parent company of Bright Arch Building, Bright Arch Plumbing and Bright Arch Renovating. We require a sophisticated business card that covers all aspects of the building and plumbing space without using told or construction items.

Industry/Entity Type

Construction Company

Contact Information for Business Card

Gareth Pimley
Director
0472915083
gareth@brightarch.com.au
Www.brightarch.com.au

Font styles to use
Serif
Sans Serif

Colors
3176b5
ffce3e
0692cd
34a7d8
fbee3e
faa54b

Requirements
Must have
• Logo on front
• Logo and details on rear.
Nice to have
• Maybe water mark or shadow effect with logo
Should not have
• Tools or any construction associated items

```html
<!DOCTYPE html>
<html lang="en">
<head>
<meta charset="UTF-8">
<title>Bright Arch Group – Business Card</title>
<link href="https://fonts.googleapis.com/css2?family=Lato:wght@300;400;700&display=swap" rel="stylesheet">
<style>
  :root {
    --backdrop: #d9d9d9;
    --card: #050505;
    --ink: #ffffff;
    --accent: #3176b5;
    --muted: #8a8a8a;
  }
  * { box-sizing: border-box; margin: 0; padding: 0; }
  html, body { width: 1200px; height: 900px; overflow: hidden; }
  body {
    background: var(--backdrop);
    font-family: "Lato", Arial, sans-serif;
    display: flex;
    flex-direction: column;
    align-items: center;
    justify-content: center;
    gap: 40px;
  }
  .card {
    width: 700px;
    height: 400px;
    background: var(--card);
    color: var(--ink);
    position: relative;
    box-shadow: 0 10px 28px rgba(0,0,0,0.35);
  }
  .brand {
    display: flex;
    align-items: center;
    gap: 14px;
  }
  .brand-dot {
    width: 18px;
    height: 18px;
    border-radius: 50%;
    background: var(--accent);
    flex: none;
  }
  .brand-name {
    font-weight: 300;
    text-transform: uppercase;
    color: var(--ink);
    white-space: nowrap;
  }

  /* Front */
  .card-front {
    display: flex;
    flex-direction: column;
    align-items: center;
    justify-content: center;
  }
  .card-front .brand-name { font-size: 40px; letter-spacing: 0.18em; }
  .card-front .brand-dot { width: 24px; height: 24px; }
  .front-url {
    margin-top: 40px;
    font-size: 17px;
    letter-spacing: 0.12em;
    color: var(--ink);
  }

  /* Back */
  .card-back {
    display: flex;
    align-items: center;
    padding: 0 50px;
  }
  .back-brand { width: 300px; }
  .card-back .brand-name { font-size: 24px; letter-spacing: 0.16em; }
  .divider {
    width: 2px;
    height: 190px;
    margin: 0 36px 0 24px;
    background: linear-gradient(to bottom, rgba(255,255,255,0), #9a9a9a 50%, rgba(255,255,255,0));
  }
  .contact-name { font-size: 30px; font-weight: 700; letter-spacing: 0.01em; }
  .contact-role { font-size: 20px; color: var(--accent); margin: 2px 0 18px; }
  .contact-list { list-style: none; }
  .contact-list li {
    display: flex;
    align-items: center;
    gap: 12px;
    font-size: 19px;
    line-height: 1.55;
  }
  .contact-list svg { width: 16px; height: 16px; fill: var(--accent); flex: none; }
</style>
</head>
<body>
  <section class="card card-front">
    <div class="brand">
      <span class="brand-dot"></span>
      <span class="brand-name">Bright Arch Group</span>
    </div>
    <p class="front-url">www.brightarch.com.au</p>
  </section>

  <section class="card card-back">
    <div class="back-brand brand">
      <span class="brand-dot"></span>
      <span class="brand-name">Bright Arch Group</span>
    </div>
    <div class="divider"></div>
    <div class="contact">
      <h1 class="contact-name">Gareth Pimley</h1>
      <p class="contact-role">Director</p>
      <ul class="contact-list">
        <li>
          <svg viewBox="0 0 24 24" aria-hidden="true"><path d="M6.6 10.8c1.4 2.8 3.8 5.1 6.6 6.6l2.2-2.2c.3-.3.7-.4 1-.2 1.1.4 2.3.6 3.6.6.6 0 1 .4 1 1V20c0 .6-.4 1-1 1C10.6 21 3 13.4 3 4c0-.6.4-1 1-1h3.5c.6 0 1 .4 1 1 0 1.3.2 2.5.6 3.6.1.3 0 .7-.2 1z"/></svg>
          0472 915 083
        </li>
        <li>
          <svg viewBox="0 0 24 24" aria-hidden="true"><path d="M2 5h20v14H2z M3.5 6.5 12 13l8.5-6.5" fill="none" stroke="#3176b5" stroke-width="2"/><path d="M2 5h20L12 12.5z"/></svg>
          gareth@brightarch.com.au
        </li>
        <li>
          <svg viewBox="0 0 24 24" aria-hidden="true"><path d="M12 2a10 10 0 1 0 0 20 10 10 0 0 0 0-20zm6.9 9h-3c-.1-2.4-.6-4.5-1.4-6a8 8 0 0 1 4.4 6zM12 4c.9 1.2 1.7 3.6 1.9 7h-3.8c.2-3.4 1-5.8 1.9-7zM9.5 5c-.8 1.5-1.3 3.6-1.4 6h-3a8 8 0 0 1 4.4-6zM5.1 13h3c.1 2.4.6 4.5 1.4 6a8 8 0 0 1-4.4-6zM12 20c-.9-1.2-1.7-3.6-1.9-7h3.8c-.2 3.4-1 5.8-1.9 7zm2.5-1c.8-1.5 1.3-3.6 1.4-6h3a8 8 0 0 1-4.4 6z"/></svg>
          www.brightarch.com.au
        </li>
      </ul>
    </div>
  </section>
</body>
</html>
```